Smart Proposal Template

I would like to create a reusable proposal template to be used for selling business to business products or services. Please see the attached word doc. The template must have expandable/contractable fields allowing the user to populate it with data without disrupting the format.. Please see the attached sample. The red font represents sample data for guiding the user in how to complete the template. This data must be able to be removed when the user ads in their actual data.

Target Market(s)

business owners

Font styles to use
Sans Serif

Colors
ec1f27
ffffff

Requirements
Must have
• template must be a tool that allows the users to fill in the blanks.
the red font that i have is text for suggesting how the users fill in the field.
The header must allow the user to replace my title with theirs.

```html
<!DOCTYPE html>
<html lang="en">
<head>
<meta charset="utf-8">
<title>Smart Proposal Template – Spread</title>
<link rel="stylesheet" href="https://fonts.googleapis.com/css2?family=Didact+Gothic&family=Open+Sans:wght@400;800&display=swap">
<style>
  :root {
    --brand-red: #ec1f27;
    --paper: #ffffff;
    --backdrop: #e8e8e8;
    --ink: #1d1d1d;
    --ink-soft: #3a3a3a;
    --rule-dark: #3b3b3b;
    --notice-fill: #b3b3b3;
    --notice-ink: #5a5a5a;
    --spine-shadow: rgba(0,0,0,0.10);
  }
  * { box-sizing: border-box; margin: 0; padding: 0; }
  html, body {
    width: 1200px; height: 900px; overflow: hidden;
    background: var(--backdrop);
  }
  .spread {
    position: absolute; left: 70px; top: 60px;
    width: 1060px; height: 780px;
    display: flex;
    box-shadow: 0 6px 24px rgba(0,0,0,0.12);
  }
  .page {
    position: relative; width: 530px; height: 780px;
    background: var(--paper);
    padding: 56px 48px 0 52px;
    font-family: "Didact Gothic", "Century Gothic", sans-serif;
    color: var(--ink);
    font-size: 14px; line-height: 1.45;
  }
  .page--left { background: linear-gradient(to left, var(--spine-shadow), transparent 40px), var(--paper); }
  .page--right { background: linear-gradient(to right, var(--spine-shadow), transparent 40px), var(--paper); }

  .guide-list { list-style: none; }
  .guide-list li { position: relative; padding-left: 22px; margin-bottom: 6px; }
  .guide-list li::before {
    content: ""; position: absolute; left: 4px; top: 8px;
    width: 5px; height: 5px; border-radius: 50%; background: var(--ink);
  }
  .guide-list--nested li { padding-left: 44px; }
  .guide-list--nested li::before { left: 26px; }

  .section-heading { position: relative; height: 62px; margin: 26px 0 18px; }
  .section-heading__stroke {
    position: absolute; right: 20px; top: 0;
    width: 330px; height: 14px; background: var(--brand-red);
    transform: skewX(-12deg);
  }
  .section-heading__tab {
    position: absolute; left: 0; top: 28px;
    display: flex; align-items: stretch; height: 28px;
  }
  .section-heading__marker { width: 8px; background: var(--rule-dark); }
  .section-heading__label {
    background: var(--brand-red);
    padding: 0 60px 0 10px;
    font-family: "Open Sans", Arial, sans-serif;
    font-weight: 800; font-size: 17px; letter-spacing: 0.02em;
    color: var(--ink); line-height: 22px;
    clip-path: polygon(0 0, 100% 12%, 98% 100%, 0 100%);
  }

  .intro { margin-bottom: 10px; }

  .rights-notice {
    position: absolute; left: 60px; right: 60px; top: 560px;
    background: var(--notice-fill);
    color: var(--notice-ink);
    font-size: 13px; line-height: 1.5;
    padding: 22px 24px;
  }

  .stakeholder-table {
    width: 100%; border: 1px solid var(--brand-red);
    border-collapse: collapse; margin: 14px 0 10px;
    font-size: 13px;
  }
  .stakeholder-table th {
    background: var(--brand-red); color: var(--ink);
    font-family: "Open Sans", Arial, sans-serif; font-weight: 800;
    text-align: left; padding: 4px 10px; font-size: 13px;
  }
  .stakeholder-table td {
    padding: 6px 10px; vertical-align: top; height: 44px;
    border-right: 1px solid var(--brand-red);
  }
  .stakeholder-table td:last-child { border-right: 0; }
  .stakeholder-table .spacer-row td { height: 110px; }
</style>
</head>
<body>
<main class="spread">

  <section class="page page--left">
    <ul class="guide-list">
      <li>Objective: Describe the primary business outcome the client expects</li>
    </ul>

    <table class="stakeholder-table">
      <thead>
        <tr><th>Role</th><th>Stakeholder/Title</th></tr>
      </thead>
      <tbody>
        <tr><td>Decision Maker</td><td>Insert corresponding stakeholders name</td></tr>
        <tr><td>Influencer</td><td>Insert corresponding stakeholders name</td></tr>
        <tr class="spacer-row"><td>End User</td><td></td></tr>
      </tbody>
    </table>

    <div class="section-heading">
      <div class="section-heading__stroke"></div>
      <div class="section-heading__tab">
        <span class="section-heading__marker"></span>
        <h2 class="section-heading__label">ALTERNATIVES CONSIDERED</h2>
      </div>
    </div>

    <ul class="guide-list">
      <li>Status quo / Do nothing - Describe why the client must take action</li>
      <li>Build internally - Describe why this is not feasible. Internal teams lack requirements or they are tied up with competing priorities</li>
    </ul>

    <p class="rights-notice">All rights reserved. No part of this information may be reproduced or transmitted without the expressed written permission of the authors. For further information contact: Northbridge Partners Inc.</p>
  </section>

  <section class="page page--right">
    <ul class="guide-list guide-list--nested">
      <li>Customization - Explain how your offering is tailored to enable best-fit</li>
      <li>Schedule/timing - Explain how the work will be completed or delivered as needed for the client</li>
      <li>Technical Alignment - Explain how your solution aligns with clients technical or installed technology environment</li>
      <li>Industry Alignment - Define how your offering aligns with the needs of the clients industry.</li>
    </ul>

    <div class="section-heading">
      <div class="section-heading__stroke"></div>
      <div class="section-heading__tab">
        <span class="section-heading__marker"></span>
        <h2 class="section-heading__label">CORPORATE OVERVIEW</h2>
      </div>
    </div>

    <p class="intro">Insert 1 paragraph that describes your organization in terms of:</p>
    <ul class="guide-list guide-list--nested">
      <li>Skills that align to this specific solution</li>
      <li>Experience in delivering similar solutions</li>
      <li>Accomplishments of similar clients of projects</li>
    </ul>

    <p class="rights-notice">All rights reserved. No part of this information may be reproduced or transmitted without the expressed written permission of the authors. For further information contact: Northbridge Partners Inc.</p>
  </section>

</main>
</body>
</html>
```